Investment company needing business card

We are wanting a business card which looks sharp and easy on the eye. We are thinking of having a business card with the logo embossed on it, to really make it stand out. We will only have a small amount of information of the business card, person's name, position, email address and phone number

Contact Information for Business Card

Danica Pruett
Executive Assistant
+64 21 547 3162
danicap@harwellcapital.co.nz

Requirements
Must have
• Embossed logo
Should not have
• Not to be busy

```html
<!DOCTYPE html>
<html lang="en">
<head>
<meta charset="utf-8">
<title>Harwell Capital – Business Card</title>
<link rel="stylesheet" href="https://fonts.googleapis.com/css2?family=Urbanist:wght@600;700&family=Roboto+Condensed:wght@700&display=swap">
<style>
  :root {
    --brand-green: #00a276;
    --ring-green: #5fbf9c;
    --ink-grey: #666666;
    --paper: #ffffff;
  }
  * { margin: 0; padding: 0; box-sizing: border-box; }
  html, body { width: 1200px; height: 720px; overflow: hidden; background: var(--paper); }
  .card { position: relative; width: 1200px; height: 720px; background: var(--paper); }

  .brand {
    position: absolute; top: 82px; left: 0; width: 1200px; height: 112px;
    display: flex; justify-content: center; align-items: center; gap: 24px;
  }
  .brand-square { width: 112px; height: 112px; background: var(--ink-grey); border-radius: 12px; flex: none; }
  .brand-name {
    font-family: "Urbanist", sans-serif; font-weight: 700; font-size: 54px; letter-spacing: 1px;
    color: var(--brand-green); line-height: 1; white-space: nowrap;
  }

  .contact-band {
    position: absolute; top: 265px; left: 0; width: 1200px; height: 375px;
    background: var(--brand-green);
  }
  .contact-item { position: absolute; top: 0; width: 400px; margin-left: -200px; text-align: center; }
  .contact-item.email { left: 261px; }
  .contact-item.phone { left: 600px; }
  .contact-item.web { left: 939px; }
  .icon-ring { display: block; margin: 50px auto 0; width: 192px; height: 192px; }
  .contact-text {
    font-family: "Roboto Condensed", sans-serif; font-weight: 700; color: var(--paper);
    margin-top: 22px; white-space: nowrap; font-size: 23px; line-height: 1.2;
  }

  .holder {
    position: absolute; top: 644px; left: 0; width: 1200px; text-align: center;
    color: var(--brand-green);
  }
  .holder-name {
    font-family: "Urbanist", sans-serif; font-weight: 700; font-size: 42px; line-height: 1;
    letter-spacing: 0.5px;
  }
  .holder-role {
    margin-top: 6px; font-family: "Urbanist", sans-serif; font-weight: 600; font-size: 17px;
    line-height: 1; letter-spacing: 2px; color: var(--ink-grey); text-transform: uppercase;
  }
</style>
</head>
<body>
<main class="card">
  <header class="brand">
    <span class="brand-square"></span>
    <span class="brand-name">HARWELL CAPITAL</span>
  </header>

  <section class="contact-band">
    <div class="contact-item email">
      <svg class="icon-ring" viewBox="0 0 192 192" aria-hidden="true">
        <circle cx="96" cy="96" r="92" fill="none" stroke="var(--ring-green)" stroke-width="4" stroke-dasharray="18 11"/>
        <path d="M96 66c-14 0-23 10-23 22 0 15 23 41 23 41s23-26 23-41c0-12-9-22-23-22z" fill="#fff"/>
        <circle cx="96" cy="87" r="9" fill="var(--brand-green)"/>
      </svg>
      <p class="contact-text">danicap@harwellcapital.co.nz</p>
    </div>

    <div class="contact-item phone">
      <svg class="icon-ring" viewBox="0 0 192 192" aria-hidden="true">
        <circle cx="96" cy="96" r="92" fill="none" stroke="var(--ring-green)" stroke-width="4" stroke-dasharray="18 11"/>
        <path d="M66 86c0-12 60-12 60 0v5h-14v-6c-8-3-24-3-32 0v6H66z" fill="#fff"/>
        <path d="M82 92h28l12 22v11H70v-11z" fill="#fff"/>
        <g fill="var(--brand-green)">
          <rect x="89" y="98" width="4" height="4"/><rect x="95" y="98" width="4" height="4"/><rect x="101" y="98" width="4" height="4"/>
          <rect x="89" y="104" width="4" height="4"/><rect x="95" y="104" width="4" height="4"/><rect x="101" y="104" width="4" height="4"/>
          <rect x="89" y="110" width="4" height="4"/><rect x="95" y="110" width="4" height="4"/><rect x="101" y="110" width="4" height="4"/>
        </g>
      </svg>
      <p class="contact-text">+64 21 547 3162</p>
    </div>

    <div class="contact-item web">
      <svg class="icon-ring" viewBox="0 0 192 192" aria-hidden="true">
        <circle cx="96" cy="96" r="92" fill="none" stroke="var(--ring-green)" stroke-width="4" stroke-dasharray="18 11"/>
        <g fill="none" stroke="#fff" stroke-width="4">
          <circle cx="96" cy="96" r="28"/>
          <ellipse cx="96" cy="96" rx="12" ry="28"/>
          <line x1="96" y1="68" x2="96" y2="124"/>
          <line x1="68" y1="96" x2="124" y2="96"/>
          <path d="M73 80h46M73 112h46"/>
        </g>
      </svg>
      <p class="contact-text">www.harwellcapital.co.nz</p>
    </div>
  </section>

  <footer class="holder">
    <h1 class="holder-name">Danica Pruett</h1>
    <p class="holder-role">Executive Assistant</p>
  </footer>
</main>
</body>
</html>
```